Summer Drinks Flyer for Coffee Shop

We are a coffee shop in London and would like to have a cool and nice flyer for our summer drinks (juices and frozen drink) flyer - see on the attached file for the list

Attached you can find an "attempt" - please note that I would no necessary need the image below.

I also attache our new logo.

thank you

Industry/Entity Type

Coffee Shop

```html
<!DOCTYPE html>
<html lang="en">
<head>
<meta charset="utf-8">
<title>Solmarea – New Summer Drinks Menu</title>
<link href="https://fonts.googleapis.com/css2?family=Mystery+Quest&family=Delius&display=swap" rel="stylesheet">
<style>
  :root {
    --canvas: #ffffff;
    --sun-yellow: #e3ec3a;
    --lime: #cfe02a;
    --orange-glow: #f2b41c;
    --sky-hint: #bfe3d6;
    --gold: #b08f2e;
    --berry: #b3212a;
    --berry-dark: #8c161d;
    --coffee: #4a2f16;
    --coffee-dark: #2f1c0b;
    --latte: #a7864c;
    --leaf: #8fb01f;
    --leaf-dark: #6c8a12;
    --olive: #4a4d12;
    --ink-soft: #3c3410;
    --white: #ffffff;
  }
  * { margin: 0; padding: 0; box-sizing: border-box; }
  html, body { width: 1000px; height: 1200px; overflow: hidden; background: var(--canvas); }
  .canvas { position: relative; width: 1000px; height: 1200px; overflow: hidden; background: var(--canvas); font-family: "Delius", cursive; }

  .flyer {
    position: absolute; left: 78px; top: 0; width: 847px; height: 1200px;
    background:
      radial-gradient(ellipse 300px 220px at 100% 6%, var(--orange-glow), transparent 70%),
      radial-gradient(ellipse 260px 320px at 0% 30%, var(--sky-hint), transparent 70%),
      linear-gradient(180deg, var(--lime) 0%, var(--sun-yellow) 28%, #eef49a 48%, #fbfde8 62%, var(--white) 72%);
  }

  .brand { position: absolute; top: 58px; left: 0; width: 1000px; display: flex; justify-content: center; align-items: center; gap: 12px; }
  .brand-dot { width: 22px; height: 22px; border-radius: 50%; background: var(--gold); }
  .brand-name { font-family: "Delius", cursive; font-size: 50px; color: var(--gold); line-height: 1; }

  .headline { position: absolute; top: 160px; left: 0; width: 1000px; text-align: center; font-family: "Mystery Quest", cursive; font-size: 92px; line-height: 100px; color: var(--gold); font-weight: 400; word-spacing: 18px; }

  .photo { position: absolute; border-radius: 14px 14px 30px 30px; }
  .photo-frozen { left: 180px; top: 345px; width: 290px; height: 490px; background: linear-gradient(180deg, #d8333f, #c62234 60%, #e4707a); }
  .photo-juice { left: 555px; top: 345px; width: 275px; height: 490px; background: linear-gradient(180deg, #e1e77a, #c9d660 60%, #7fb53a); }
  .photo-coffee { left: 392px; top: 415px; width: 258px; height: 540px; background: linear-gradient(180deg, #faf6ee 0%, #f1e6d2 14%, #c9a47a 30%, #b78c5e 80%, #d9b588 100%); }

  .ribbon { position: absolute; }
  .ribbon-label { position: absolute; left: 0; top: 0; width: 100%; height: 100%; display: flex; align-items: center; justify-content: center; color: var(--white); }
  .ribbon-frozen { left: 110px; top: 850px; width: 262px; height: 90px; }
  .ribbon-frozen .ribbon-label { font-size: 20px; transform: rotate(-5deg); }
  .ribbon-coffee { left: 388px; top: 930px; width: 255px; height: 98px; }
  .ribbon-coffee .ribbon-label { font-size: 27px; transform: rotate(-10deg); }
  .ribbon-juice { left: 657px; top: 812px; width: 260px; height: 100px; }
  .ribbon-juice .ribbon-label { font-size: 27px; transform: rotate(-10deg); }

  .menu { position: absolute; text-align: center; }
  .menu-list { list-style: none; font-size: 19px; line-height: 26px; }
  .price { font-size: 36px; line-height: 1; margin-top: 18px; }
  .note { font-size: 15px; color: var(--ink-soft); margin-top: 12px; }

  .menu-frozen { left: 115px; top: 965px; width: 260px; color: var(--berry); }
  .menu-frozen .menu-list { line-height: 28px; }
  .menu-frozen .price { color: var(--berry); margin-top: 22px; }

  .menu-coffee { left: 385px; top: 1033px; width: 260px; color: var(--latte); }
  .menu-coffee .menu-list { font-size: 18px; line-height: 22px; }
  .menu-coffee .price { color: var(--coffee-dark); margin-top: 14px; }

  .menu-juice { left: 655px; top: 930px; width: 260px; color: var(--leaf); }
  .menu-juice .menu-list { line-height: 26px; }
  .menu-juice .price { color: var(--olive); margin-top: 14px; }
</style>
</head>
<body>
<div class="canvas">
  <main class="flyer"></main>

  <header class="brand">
    <span class="brand-dot"></span>
    <span class="brand-name">solmarea</span>
  </header>

  <h1 class="headline">New Summer<br>Drinks Menu</h1>

  <div class="photo photo-frozen" role="img" aria-label="Photo of a frozen strawberry drink topped with a strawberry, with berries and a red splash beside it"></div>
  <div class="photo photo-juice" role="img" aria-label="Photo of a green kiwi juice with a kiwi slice, halved kiwis and a green splash beside it"></div>
  <div class="photo photo-coffee" role="img" aria-label="Photo of an iced coffee with whipped cream, coffee beans and ground coffee at its base"></div>

  <div class="ribbon ribbon-frozen">
    <svg width="262" height="90" viewBox="0 0 262 90">
      <path d="M4 46 L240 22 L224 44 L258 72 L22 84 L36 66 Z" fill="var(--berry-dark)"/>
      <path d="M10 38 L232 16 L236 64 L18 80 Z" fill="var(--berry)"/>
    </svg>
    <span class="ribbon-label">Frozen Fruit Drinks</span>
  </div>

  <div class="ribbon ribbon-coffee">
    <svg width="255" height="98" viewBox="0 0 255 98">
      <path d="M4 70 L232 10 L218 34 L252 60 L28 96 L40 80 Z" fill="var(--coffee-dark)"/>
      <path d="M12 60 L226 6 L236 56 L20 92 Z" fill="var(--coffee)"/>
    </svg>
    <span class="ribbon-label">Iced-Coffees</span>
  </div>

  <div class="ribbon ribbon-juice">
    <svg width="260" height="100" viewBox="0 0 260 100">
      <path d="M4 66 L236 6 L222 30 L256 60 L26 98 L40 80 Z" fill="var(--leaf-dark)"/>
      <path d="M12 56 L230 4 L240 54 L20 92 Z" fill="var(--leaf)"/>
    </svg>
    <span class="ribbon-label">Fruit Juices</span>
  </div>

  <section class="menu menu-frozen">
    <ul class="menu-list">
      <li>Strawberry and banana</li>
      <li>Pineapple, mango</li>
      <li>and banana</li>
    </ul>
    <p class="price">£2.95</p>
  </section>

  <section class="menu menu-coffee">
    <ul class="menu-list">
      <li>Iced Coffee</li>
      <li>Iced Latte</li>
      <li>Iced Chocolate Drink</li>
    </ul>
    <p class="price">£2.95</p>
    <p class="note">add syrup shot for 10p</p>
  </section>

  <section class="menu menu-juice">
    <ul class="menu-list">
      <li>Orange and carrot</li>
      <li>Orange and pineapple</li>
      <li>Pineapple and apple</li>
      <li>Apple and kiwi</li>
      <li>Carrot and ginger</li>
    </ul>
    <p class="price">£2.45</p>
    <p class="note">add mint or ginger for free</p>
  </section>
</div>
</body>
</html>
```